Flyer for Cutting Edge Professional Learning Organization for Education Leaders

We need a two page, eye catching flyer that grabs the attention of busy school and district education leaders. It will communicate the exciting professional learning experiences that we are offering during the next school year.

We have included our two page flyer from last year. As you'll see the second page is virtually all text, so very easy to design that.

You can replicate the format of last year's flyer (KL SEVIN 2016-17 Menu Final), making the various text changes and additions which we have included in our word document (KL SEVIN 2017-18 Programming Flyer). Or you can go with a new format. We are open to your creativity. We are also open to either a new image that communicates the concept of leadership or one that is similar to the one we used on the first page of last year's flyer.

Target Market(s)

School and district education leaders

Industry/Entity Type

Education

Contact Information for Business Card

Logo
Lo Wendell
Executive/Program Director
lo.wendell@mqtn.example
720-555-0148
4120 Quillmoor Road
Boulder, CO 80000

Font styles to use
Sans Serif

Colors
0255a3
ffffff
3176b5

Requirements
Must have
• My flyer must have the exact text which I have included on the Word document called KL SEVIN 2017-18 Programming Flyer. We do not have time to make lots of edits and corrections to text.
• Sharp, professional and creative look.
Should not have
• No spelling or punctuation errors.

```html
<!DOCTYPE html>
<html lang="en">
<head>
<meta charset="utf-8">
<title>KL SEVIN 2017-18 Programming Flyer</title>
<link href="https://fonts.googleapis.com/css2?family=Saira+Condensed:wght@400;500&display=swap" rel="stylesheet">
<style>
  :root {
    --blue-deep: #0255a3;
    --blue-mid: #3176b5;
    --white: #ffffff;
    --ink: #1a1a1a;
    --bubble: #8a8a8a;
  }
  * { box-sizing: border-box; margin: 0; padding: 0; }
  html, body { width: 849px; height: 1200px; overflow: hidden; background: var(--white); }
  .flyer {
    position: relative;
    width: 849px;
    height: 1200px;
    background: var(--white);
    font-family: "Saira Condensed", "Arial Narrow", sans-serif;
    color: var(--ink);
  }
  .band {
    position: absolute;
    left: 0;
    width: 849px;
    display: flex;
    align-items: center;
    justify-content: center;
    background: linear-gradient(180deg, var(--blue-mid) 0%, var(--blue-deep) 100%);
    color: var(--white);
    font-weight: 500;
    font-size: 31px;
    letter-spacing: 0.3px;
  }
  .band::after {
    content: "";
    position: absolute;
    inset: 3px;
    border: 1.5px solid rgba(255,255,255,0.85);
  }
  .band--top { top: 0; height: 52px; font-size: 30px; }
  .band--shared { top: 64px; height: 42px; }
  .band--team { top: 336px; height: 42px; }
  .band--creative { top: 625px; height: 44px; width: 588px; }
  .band--pilot { top: 846px; height: 46px; font-size: 30px; }

  .region {
    position: absolute;
    left: 6px;
    width: 836px;
    display: flex;
    flex-direction: column;
    gap: 12px;
  }
  .region--shared { top: 114px; }
  .region--team { top: 386px; }
  .region--creative { top: 683px; width: 578px; }
  .region--pilot { top: 900px; gap: 10px; }

  .offering h3 {
    font-weight: 500;
    font-size: 22px;
    line-height: 27px;
    color: var(--blue-mid);
    margin-bottom: 2px;
  }
  .offering p { font-size: 16px; line-height: 21.5px; }

  .quote {
    position: absolute;
    left: 598px;
    top: 620px;
    width: 234px;
    height: 190px;
  }
  .quote svg { position: absolute; inset: 0; }
  .quote p {
    position: relative;
    padding: 14px 16px 0 18px;
    font-size: 15px;
    line-height: 19px;
    color: var(--white);
  }
  .quote .attribution { padding-top: 12px; }
</style>
</head>
<body>
<div class="flyer">

  <div class="band band--top">“Go to klsevin.example for session dates, details and facilitator bios.”</div>

  <div class="band band--shared">“Shared Classroom Challenges”</div>
  <div class="region region--shared">
    <section class="offering">
      <h3>K-12 and Preschool Instructional Rounds</h3>
      <p>Join other Metro Denver educator to hear diverse perspectives, challenge your thinking, and deepen your understanding of effective instruction and instructional leadership as you observe, discuss and reflect on key instructional challenges in K-12 and preschool classrooms.&nbsp; $30/session.</p>
    </section>
    <section class="offering">
      <h3>Early Literacy Systems Learning Community</h3>
      <p>Discover how systems improvement frameworks can enhance the structures, processes and mindsets that impact early literacy results. Receive coaching and support from facilitators and learning community members as you use the frameworks to strengthen your early literacy results.&nbsp; No fee.</p>
    </section>
  </div>

  <div class="band band--team">“Team Leadership”</div>
  <div class="region region--team">
    <section class="offering">
      <h3>Feedback Fundamentals</h3>
      <p>Through hands-on collaborative sessions, you will learn about the art and science of feedback, from cultivating a coaching mindset to practical techniques for strengthening your delivery.&nbsp; Along the way, you will build lasting relationships with a cohort of peers from across metro Denver.&nbsp; Fee is $500.&nbsp; This year we are offering two additional, optional sessions focusing on feedback in the context of conflict and organizational change.&nbsp; Additional fee is $200.</p>
    </section>
    <section class="offering">
      <h3>Leading Teams to the Top of Their Game</h3>
      <p>Connect with other Metro Denver education leaders as you generate new self-insights and gain powerful tools for more effective team leadership.&nbsp; This experience uses participants’ current team leadership challenges as the source for much of the cohort’s discussion.&nbsp; Fee is $500</p>
    </section>
  </div>

  <div class="band band--creative">“Creative Solutions”</div>
  <div class="region region--creative">
    <section class="offering">
      <h3>Design Thinking &amp; Creative Leadership</h3>
      <p>Our hallmark learning experiences!&nbsp; Draw upon your imagination, intuition, and creative reasoning to think differently about problems of practice in order to make positive change in classrooms, schools, and departments.&nbsp; Through this unique solution building method and with coaching support, you will put your own creative leadership into action.<br>Course fee is $150.&nbsp; Facilitation and coaching fees vary.</p>
    </section>
  </div>

  <aside class="quote">
    <svg viewBox="0 0 234 190" width="234" height="190" aria-hidden="true">
      <path d="M14 0 H220 Q234 0 234 14 V150 Q234 164 220 164 H80 L54 190 L58 164 H14 Q0 164 0 150 V14 Q0 0 14 0 Z" fill="var(--bubble)"/>
    </svg>
    <p>“The Design Thinking experience helped me see the great resources that surround me...my colleagues and all of our imaginations.”</p>
    <p class="attribution">- Design Thinking participant</p>
  </aside>

  <div class="band band--pilot">“2017-18 Pilot Programs - No fee for Pilot Participants”</div>
  <div class="region region--pilot">
    <section class="offering">
      <h3>Student-Driven Learning Hub</h3>
      <p>Design and pilot creative ways to help your staff foster student-driven learning environments.&nbsp; Build new relationships with local, regional and national peers as you experiment with new strategies and reflect on their effectiveness.</p>
    </section>
    <section class="offering">
      <h3>Front Range Principals Club</h3>
      <p>Join principals from across the Front Range to discuss current education issues, exchange resources, and discover helpful leadership tools. Business leaders will be invited to some club events. Club members will determine the club’s specific activities.</p>
    </section>
    <section class="offering">
      <h3>Opportunities for Highly Experienced Leaders</h3>
      <p>Work with other well-respected education leaders as you choose from an exciting menu of learning experiences that will help you elevate your leadership.&nbsp; Opportunities might include partnerships outside of education, stretch-to-learn experiences, and empathy experiences with students.</p>
    </section>
  </div>

</div>
</body>
</html>
```